agricultural technology company needs business cards*

design a business card that represents our business well. please see our website: vastrelbyfieldseal.com.au
professional, simple, clean lines, not complicated or floral.....

```html
<!DOCTYPE html>
<html lang="en">
<head>
<meta charset="utf-8">
<title>Vastrelby Fieldseal – Business Card</title>
<link href="https://fonts.googleapis.com/css2?family=Arimo:wght@400;700&display=swap" rel="stylesheet">
<style>
  :root {
    --backdrop: #8a898c;
    --navy: #192b5a;
    --navy-deep: #0f2352;
    --leaf-green: #22b24c;
    --text-grey: #4a4a4a;
    --white: #ffffff;
  }
  * { margin: 0; padding: 0; box-sizing: border-box; }
  html, body {
    width: 1200px; height: 818px; overflow: hidden;
    background: var(--backdrop);
    font-family: "Arimo", Arial, sans-serif;
  }
  .canvas { position: relative; width: 1200px; height: 818px; }
  .card {
    position: absolute; left: 332px; width: 480px; height: 274px; overflow: hidden;
  }
  .card--front { top: 121px; background: var(--white); }
  .card--back { top: 424px; background: var(--navy); }
  .card__shape { position: absolute; inset: 0; width: 480px; height: 274px; }

  .brand-name {
    position: absolute; left: 220px; top: 48px;
    color: var(--navy); font-weight: 700; font-size: 29px; line-height: 29px;
    letter-spacing: -0.5px;
  }

  .person { position: absolute; left: 28px; top: 154px; }
  .person__name { color: var(--navy); font-weight: 700; font-size: 16px; line-height: 20px; }
  .person__title { color: var(--leaf-green); font-size: 11px; line-height: 14px; }

  .contact { position: absolute; left: 28px; top: 193px; list-style: none; }
  .contact__item {
    display: flex; align-items: center; gap: 5px;
    color: var(--text-grey); font-size: 11px; line-height: 13.5px;
  }
  .contact__icon { width: 9px; height: 9px; fill: var(--navy); flex: none; }
  .address {
    position: absolute; left: 28px; top: 239px;
    color: var(--text-grey); font-size: 11px;
  }

  .back-brand {
    position: absolute; left: 43px; top: 150px;
    color: var(--white); font-weight: 700; font-size: 36px; line-height: 36px;
    letter-spacing: -0.8px;
  }
  .back-url {
    position: absolute; left: 46px; top: 229px;
    color: var(--white); font-size: 10px; letter-spacing: 2.6px;
  }
</style>
</head>
<body>
<main class="canvas">
  <section class="card card--front" aria-label="Business card front">
    <svg class="card__shape" viewBox="0 0 480 274" aria-hidden="true">
      <polygon points="337,0 480,0 480,139" fill="var(--navy-deep)"/>
    </svg>
    <div class="brand-name">Vastrelby<br>Fieldseal</div>
    <div class="person">
      <div class="person__name">Joren Vandermaal</div>
      <div class="person__title">Founder &amp; co-owner</div>
    </div>
    <ul class="contact">
      <li class="contact__item">
        <svg class="contact__icon" viewBox="0 0 10 10"><path d="M2 0.5 3.6 2.6 2.7 3.6Q3.8 6 6.4 7.3L7.4 6.4 9.5 8 8.6 9.5Q4.5 9.3 0.6 1.4Z"/></svg>
        1300 482 617
      </li>
      <li class="contact__item">
        <svg class="contact__icon" viewBox="0 0 10 10"><path d="M0 2h10v6H0z M0.6 2.3 5 5.6 9.4 2.3" fill="var(--navy)"/><path d="M0.8 2.6 5 5.7 9.2 2.6" stroke="#fff" stroke-width="0.9" fill="none"/></svg>
        info@vastrelbyfs.com
      </li>
      <li class="contact__item">
        <svg class="contact__icon" viewBox="0 0 10 10"><circle cx="5" cy="5" r="4.8"/><path d="M2.2 3.2 4 2.6 4.6 4.2 3.2 5.4Z M5.8 6 7.6 5.6 7 8 5.6 7.6Z" fill="#fff"/></svg>
        www.vastrelbyfs.com
      </li>
    </ul>
    <div class="address">14 Harrow Lane, Kellmore, WA 6190</div>
  </section>

  <section class="card card--back" aria-label="Business card back">
    <svg class="card__shape" viewBox="0 0 480 274" aria-hidden="true">
      <polygon points="204,0 480,0 480,274" fill="var(--leaf-green)"/>
    </svg>
    <div class="back-brand">Vastrelby<br>Fieldseal</div>
    <div class="back-url">www.vastrelbyfieldseal.com.au</div>
  </section>
</main>
</body>
</html>
```